Design for a Note buying company that attracts landlords and seller financed notes

I need a card designed. I want a simple clean front with my logo and contact info. On the back I want some big and bold words to get a message across.

Our Company buys Notes (mortgages) and we want to convey the sense of financial security. Our number one market that we pursue is tired landlords.

If you want to understand our business you can visit our website. www.deedpaperlane.com

Do not use any Clip Art in the design, it will not be accepted. I want a custom designed card not something I could throw together myself. Simple clean and drive the message home.

Target Market(s)

Landlords, seller financed note holders

Industry/Entity Type

Mortgage

Contact Information for Business Card

Simple clean and bold. I need to grab the attention of the customer. It should convey a professional touch.

Font styles to use
Sans Serif

Colors
ec2229
ffffff

Requirements
Must have
• Clean front with logo and contact information
Front colors should match logo

Back should be bold and grab attention. Back colors are open to ideas
Nice to have
• The Back May use the phrase "No more Tentants, No more Toilets" "More Time, More Cash"

I'm open to other ideas about grabbing a landlords attention

I'm open to a square card design
I like cards with round corners as well
Should not have
• any clip art! must be custom designs.

```html
<!DOCTYPE html>
<html lang="en">
<head>
<meta charset="UTF-8">
<title>Larkmoor Note Buyers – Business Card</title>
<link rel="stylesheet" href="https://fonts.googleapis.com/css2?family=Montserrat:wght@400;500;700;800&display=swap">
<style>
  :root {
    --brand-red: #ec2229;
    --paper-white: #ffffff;
    --ink-black: #111111;
    --backdrop: #2a2a2a;
    --card-radius: 30px;
  }
  * { margin: 0; padding: 0; box-sizing: border-box; }
  html, body {
    width: 1200px; height: 1200px; overflow: hidden;
    background: var(--backdrop);
    font-family: "Montserrat", sans-serif;
  }
  .canvas {
    width: 1200px; height: 1200px;
    display: flex; flex-direction: column;
    align-items: center; justify-content: center; gap: 60px;
  }
  .card {
    width: 900px; height: 514px;
    border-radius: var(--card-radius);
    position: relative; overflow: hidden;
    box-shadow: 0 18px 40px rgba(0,0,0,0.45);
  }
  /* Front */
  .card--front { background: var(--paper-white); }
  .brand {
    position: absolute; left: 0; right: 0; top: 150px;
    text-align: center; color: var(--ink-black);
  }
  .brand__tagline {
    font-size: 17px; font-weight: 500; letter-spacing: 0.55em;
    margin-bottom: 18px;
  }
  .brand__name {
    font-size: 76px; font-weight: 800; line-height: 1; letter-spacing: 0.02em;
  }
  .brand__sub {
    font-size: 32px; font-weight: 800; letter-spacing: 0.35em;
    margin-top: 16px;
  }
  .front__band {
    position: absolute; left: 0; right: 0; bottom: 0; height: 62px;
    background: var(--brand-red); color: var(--paper-white);
    display: flex; align-items: center; justify-content: center;
    font-size: 22px; font-weight: 700; letter-spacing: 0.02em;
  }
  /* Back */
  .card--back { background: var(--brand-red); color: var(--paper-white); }
  .contact {
    position: absolute; left: 80px; bottom: 70px;
  }
  .contact__name {
    font-size: 40px; font-weight: 700; letter-spacing: 0.01em;
    margin-bottom: 14px;
  }
  .contact__line {
    font-size: 20px; font-weight: 400; line-height: 1.45;
  }
  .contact__list { list-style: none; margin-top: 12px; }
  .contact__item {
    display: flex; align-items: center; gap: 12px;
    font-size: 20px; line-height: 1.6;
  }
  .contact__item svg { width: 18px; height: 18px; flex: none; }
  .contact__item strong { font-weight: 700; }
</style>
</head>
<body>
<main class="canvas">
  <section class="card card--front" aria-label="Card front">
    <div class="brand">
      <p class="brand__tagline">WE HELP PEOPLE LIVE!</p>
      <p class="brand__name">LARKMOOR</p>
      <p class="brand__sub">NOTE BUYERS</p>
    </div>
    <div class="front__band">MORE TIME, MORE CASH</div>
  </section>

  <section class="card card--back" aria-label="Card back">
    <div class="contact">
      <h1 class="contact__name">MARCUS HALE</h1>
      <p class="contact__line">Larkmoor Investors Group</p>
      <p class="contact__line">P.O. Box 82 Fernhill, Ohio 44310</p>
      <ul class="contact__list">
        <li class="contact__item">
          <svg viewBox="0 0 24 24" fill="none" stroke="currentColor" stroke-width="2"><path d="M5 3h4l2 5-3 2a12 12 0 0 0 6 6l2-3 5 2v4a2 2 0 0 1-2 2A17 17 0 0 1 3 5a2 2 0 0 1 2-2z"/></svg>
          555-014-2287
        </li>
        <li class="contact__item">
          <svg viewBox="0 0 24 24" fill="none" stroke="currentColor" stroke-width="2"><rect x="3" y="5" width="18" height="14" rx="1"/><path d="M3 6l9 7 9-7"/></svg>
          info@deedpaperlane.com
        </li>
        <li class="contact__item">
          <svg viewBox="0 0 24 24" fill="none" stroke="currentColor" stroke-width="2"><circle cx="12" cy="12" r="9"/><path d="M3 12h18M12 3c3 3 3 15 0 18M12 3c-3 3-3 15 0 18"/></svg>
          <span>www.<strong>deedpaperlane</strong>.com</span>
        </li>
      </ul>
    </div>
  </section>
</main>
</body>
</html>
```